Harbourline Green Jack Socials - Flyer

So now that i have the logo, I need a flyer made up for printing to be delivered to businesses and residential homes.
Below is some information that I want included in the design, in any order and in anyway.
What better way to spend time with family, friends or workmates then to enjoy 2 hours of barefoot bowls.
We can cater for Xmas Parties, Buck's and Hen's Parties, Birthday Parties, Team Building events.
We have food and drink packages to suit all your needs.
So why not come along and have the best fun you can have on 2 feet!
We have 2 locations at Wendlebrook Sports and Bowling Club and Mossvale Ridge Bowling Club
Prices start from $12pp for 2 hours of lawn bowls fun
Contact Colin Parrow on 0478 615 240 or visit our website www.greenjacksocials-example.com.au for more information and to enquire about your function today!

```html
<!DOCTYPE html>
<html lang="en">
<head>
<meta charset="utf-8">
<title>Harbourline Green Jack Socials – Flyer</title>
<link rel="stylesheet" href="https://fonts.googleapis.com/css2?family=Alfa+Slab+One&family=Josefin+Sans:wght@400;600&display=swap">
<style>
  :root {
    --grass-dark: #1f4a12;
    --grass-mid: #3f7d22;
    --grass-light: #6aa83a;
    --white: #ffffff;
    --yellow: #f5d21c;
    --bowl-dark: #1c1f1c;
    --bowl-mid: #3a3f3a;
  }
  * { margin: 0; padding: 0; box-sizing: border-box; }
  html, body { width: 849px; height: 1200px; overflow: hidden; }
  body { font-family: "Josefin Sans", sans-serif; color: var(--white); }
  .flyer {
    position: relative;
    width: 849px;
    height: 1200px;
    overflow: hidden;
    text-align: center;
  }
  .lawn-photo {
    position: absolute; inset: 0;
    background: radial-gradient(ellipse at 50% 45%, var(--grass-light) 0%, var(--grass-mid) 45%, var(--grass-dark) 100%);
  }
  .bowls-photo {
    position: absolute;
    left: 566px; top: 930px;
    width: 283px; height: 270px;
    background: radial-gradient(ellipse at 55% 60%, var(--bowl-mid) 0%, var(--bowl-dark) 60%, rgba(28,31,28,0) 75%);
  }
  .content { position: relative; z-index: 1; }
  .brand-title {
    font-family: "Alfa Slab One", serif;
    font-weight: 400;
    color: var(--white);
    text-transform: uppercase;
    line-height: 1;
    padding-top: 36px;
  }
  .brand-title .line-1 { display: block; font-size: 56px; letter-spacing: 2px; }
  .brand-title .line-2 { display: block; font-size: 92px; margin-top: 8px; }
  .brand-title .line-3 { display: block; font-size: 66px; margin-top: 8px; }
  .tagline {
    margin-top: 28px;
    font-size: 31px;
    font-weight: 600;
    color: var(--yellow);
    text-transform: uppercase;
  }
  .details {
    width: 600px;
    margin: 26px auto 0;
    font-size: 19px;
    line-height: 1.35;
    text-transform: uppercase;
  }
  .details p + p { margin-top: 22px; }
  .invite {
    width: 600px;
    margin: 34px auto 0;
    font-size: 27px;
    line-height: 1.3;
    text-transform: uppercase;
  }
  .price {
    width: 600px;
    margin: 30px auto 0;
    font-size: 22px;
    line-height: 1.35;
    text-transform: uppercase;
  }
  .contact {
    position: absolute;
    left: 28px; top: 996px;
    text-align: left;
    text-transform: uppercase;
  }
  .contact-label { font-size: 27px; color: var(--yellow); }
  .contact-row { font-size: 27px; line-height: 1.3; }
  .contact-row .phone { color: var(--yellow); }
  .website {
    position: absolute;
    left: 28px; top: 1110px;
    font-size: 28px;
    font-weight: 600;
    color: var(--yellow);
    text-transform: uppercase;
  }
</style>
</head>
<body>
  <main class="flyer">
    <div class="lawn-photo" role="img" aria-label="Close-up photograph of a mown bowling green lawn"></div>
    <div class="bowls-photo" role="img" aria-label="Photograph of two dark lawn bowls resting on the grass"></div>

    <div class="content">
      <h1 class="brand-title">
        <span class="line-1">Harbourline</span>
        <span class="line-2">Green Jack</span>
        <span class="line-3">Socials</span>
      </h1>

      <p class="tagline">The most fun you can have on 2 feet!</p>

      <section class="details">
        <p>Lawn bowls was once seen has a older persons sport, not any longer with the craze of barefoot bowls taking over.</p>
        <p>What better way to spend an afternoon with friends or workmates?</p>
        <p>We can cater for hen's and buck's parties, birthday celebrations, team building and corporate events as well as Xmas parties</p>
        <p>We have two venues available at Wendlebrook Sports and Bowling Club and Mossvale Ridge Bowling Club</p>
      </section>

      <p class="invite">Come along and have the best fun you can have on two feet!</p>

      <p class="price">Prices start from as a little as $12pp for 2 hours of lawn bowls fun</p>
    </div>

    <section class="contact">
      <p class="contact-label">Contact</p>
      <p class="contact-row">Colin Parrow &nbsp;: <span class="phone">0478 615 240</span></p>
      <p class="contact-row">Marla Fenwick : <span class="phone">0461 308 527</span></p>
    </section>

    <p class="website">www.greenjacksocials-example.com.au</p>
  </main>
</body>
</html>
```